Bramblewood Counselling Group Pty Ltd

clinical psychologist in private practice needs professional stationery package: business cards, complimentary slips, envelopes, range of business letterheads, and logo (photo of lighthouse).

I work with children, adolescents, adults and older population with a range of mental health concerns, adjustment to life transitions and learning difficulties. Majority of my correspondence is with medical practitioners writing reports. I would a clean crisp professional presentation (white background, navy blue text but open to ideas). Thought about having lighthouse as watermark on envelopes. My professional organisation (GTC) logo needs to be on business cards and templates (manual gives guidelines),. The photo of lighthouse is to be included in logo.
There needs to be three letterheads. 1.Is Company only Detail "bramblewood Counselling Group Pty Ltd". 2. Include Company detail and Moira Fensham Clinical Psychologist information at KVRT. 3. Include Company detail and Moira Fensham Clinical Psychologist information at Orchardvale Medical Centre

Target Market(s)

Doctors

Industry/Entity Type

Business

Colors
0355a3
3176b5
0592cd
33a6d7

Requirements
Must have
• Picture of the lighthouse
• GTC logo
• Business name

```html
<!DOCTYPE html>
<html lang="en">
<head>
<meta charset="utf-8">
<title>Bramblewood Counselling Group Pty Ltd – Envelopes</title>
<link rel="stylesheet" href="https://fonts.googleapis.com/css2?family=Tinos&family=Open+Sans:wght@400&display=swap">
<style>
  :root {
    --page: #ececec;
    --paper: #f6f6f6;
    --navy: #0355a3;
    --mid: #3176b5;
    --sky: #0592cd;
    --ink: #111111;
    --fold: #dcdcdc;
  }
  * { margin: 0; padding: 0; box-sizing: border-box; }
  html, body { width: 1200px; height: 1147px; overflow: hidden; background: var(--page); }
  .envelope {
    position: absolute;
    left: 149px;
    width: 906px;
    background: var(--paper);
    overflow: hidden;
  }
  .envelope--back { top: 130px; height: 431px; }
  .envelope--front { top: 597px; height: 433px; }
  .flap-line { position: absolute; left: 0; top: 0; }
  .brand { position: absolute; display: flex; align-items: flex-start; gap: 14px; }
  .envelope--back .brand { left: 268px; top: 38px; }
  .envelope--front .brand { left: 38px; top: 48px; }
  .brand__mark { width: 56px; height: 56px; background: var(--navy); flex: none; margin-top: 4px; }
  .brand__text { font-family: "Tinos", "Times New Roman", serif; }
  .brand__name { font-size: 28px; line-height: 32px; color: var(--navy); font-weight: 400; }
  .brand__tagline { margin-top: 8px; font-size: 12px; color: var(--sky); white-space: nowrap; }
  .return-address {
    position: absolute; left: 108px; top: 148px;
    font-family: "Open Sans", Arial, sans-serif;
    font-size: 17px; color: var(--ink);
  }
  .base-band { position: absolute; left: 0; bottom: 0; }
</style>
</head>
<body>
  <section class="envelope envelope--back" aria-label="Envelope back">
    <svg class="flap-line" width="906" height="160" viewBox="0 0 906 160">
      <path d="M10 0 L10 140 Q10 150 22 150 L884 150 Q896 150 896 140 L896 0" fill="none" stroke="var(--fold)" stroke-width="1.5"/>
    </svg>
    <div class="brand">
      <div class="brand__mark"></div>
      <div class="brand__text">
        <p class="brand__name">Bramblewood Counselling<br>Group Pty Ltd</p>
        <p class="brand__tagline">Therapy and assessment for children, adolescents and adults</p>
      </div>
    </div>
  </section>

  <section class="envelope envelope--front" aria-label="Envelope front">
    <div class="brand">
      <div class="brand__mark"></div>
      <div class="brand__text">
        <p class="brand__name">Bramblewood Counselling<br>Group Pty Ltd</p>
        <p class="brand__tagline">Therapy and assessment for children, adolescents and adults</p>
      </div>
    </div>
    <p class="return-address">PO Box 812, Fernleigh, Q4361.</p>
    <svg class="base-band" width="906" height="90" viewBox="0 0 906 90">
      <defs>
        <linearGradient id="bandFill" x1="0" x2="1" y1="0" y2="0">
          <stop offset="0" stop-color="var(--navy)"/>
          <stop offset="1" stop-color="var(--mid)"/>
        </linearGradient>
      </defs>
      <path d="M0 50 Q453 10 906 40 L906 90 L0 90 Z" fill="url(#bandFill)"/>
    </svg>
  </section>
</body>
</html>
```